Moving Company Needs Business Card Design

We need a business cars for moving company based in San Diego. We are called Harborline Relocation Group. We move locally and long distance. 1st side: Logo, website: www.HarborlineRelo.com, Telephone number: 1-855-314-7068.
2nd side: Licensed and Insured,
We move homes and businesses
Services: Local Moving, Long Distance Moving, Loading / Unloading your truck / container, On-site Moving, Packing Service
telephone number 1-855-314-7068, email: info@harborlinerelo.com

```html
<!DOCTYPE html>
<html lang="en">
<head>
<meta charset="utf-8">
<title>Harborline Relocation Group – Business Card</title>
<link href="https://fonts.googleapis.com/css2?family=Open+Sans:wght@400;600;700&display=swap" rel="stylesheet">
<style>
  :root {
    --page-bg: #e9e9ea;
    --card-bg: #ffffff;
    --navy: #1b3f7f;
    --blue: #0b63ad;
    --red: #d71f2b;
    --red-deep: #9e1a22;
    --ink: #1d2430;
    --white: #ffffff;
  }
  * { box-sizing: border-box; margin: 0; padding: 0; }
  html, body {
    width: 1200px; height: 900px; overflow: hidden;
    background: var(--page-bg);
    font-family: "Open Sans", Arial, sans-serif;
  }
  .canvas {
    position: relative; width: 1200px; height: 900px;
    display: flex; flex-direction: column; align-items: center; justify-content: center; gap: 40px;
  }
  .card {
    position: relative; width: 700px; height: 400px;
    background: var(--card-bg);
    box-shadow: 0 6px 18px rgba(0,0,0,0.15);
    overflow: hidden;
  }
  .card-art { position: absolute; inset: 0; width: 100%; height: 100%; }

  /* Information side */
  .tagline {
    position: absolute; left: 62px; top: 34px;
    font-size: 19px; font-weight: 700; color: var(--ink);
  }
  .contact-list { position: absolute; left: 62px; top: 78px; list-style: none; }
  .contact-list li {
    display: flex; align-items: center; gap: 10px;
    font-size: 13px; color: var(--ink); margin-bottom: 8px;
  }
  .contact-list svg { width: 16px; height: 14px; }
  .licensed {
    position: absolute; left: 62px; top: 148px;
    font-size: 19px; color: var(--white); letter-spacing: 0.3px;
  }
  .services {
    position: absolute; right: 48px; top: 200px; text-align: right; color: var(--ink);
  }
  .services h2 { font-size: 28px; font-weight: 700; margin-bottom: 14px; }
  .services ul { list-style: none; }
  .services li { font-size: 17px; line-height: 1.5; }

  /* Brand side */
  .brand-name {
    position: absolute; left: 50px; top: 120px; width: 330px;
    font-size: 38px; font-weight: 700; line-height: 1.1; color: var(--red);
  }
  .brand-contact {
    position: absolute; right: 90px; top: 300px; text-align: center;
    color: var(--white); font-size: 22px; line-height: 1.3;
  }
</style>
</head>
<body>
<main class="canvas">

  <section class="card card-info" aria-label="Card back with services">
    <svg class="card-art" viewBox="0 0 700 400" aria-hidden="true">
      <defs>
        <linearGradient id="blueBand" x1="0" y1="0" x2="0" y2="1">
          <stop offset="0" stop-color="var(--blue)"/>
          <stop offset="1" stop-color="var(--navy)"/>
        </linearGradient>
        <linearGradient id="redSwoosh" x1="0" y1="1" x2="1" y2="0">
          <stop offset="0" stop-color="var(--red-deep)"/>
          <stop offset="0.5" stop-color="var(--red)"/>
          <stop offset="1" stop-color="var(--red)"/>
        </linearGradient>
      </defs>
      <polygon points="0,0 645,0 615,18 0,18" fill="url(#blueBand)"/>
      <path d="M0 140 L330 140 C 220 205, 90 300, 0 378 Z" fill="url(#blueBand)"/>
      <path d="M0 400 L0 394 C 200 230, 420 80, 645 6 C 470 95, 300 225, 200 400 Z" fill="url(#redSwoosh)"/>
    </svg>
    <p class="tagline">We move homes and businesses</p>
    <ul class="contact-list">
      <li>
        <svg viewBox="0 0 16 14" aria-hidden="true"><path d="M1 4 C1 1 15 1 15 4 L12 5 L11 3 L5 3 L4 5 Z M3 6 L13 6 L14 13 L2 13 Z" fill="var(--ink)"/></svg>
        1-855-314-7068
      </li>
      <li>
        <svg viewBox="0 0 16 14" aria-hidden="true"><rect x="1" y="2" width="14" height="10" fill="none" stroke="var(--ink)" stroke-width="1.6"/><path d="M1 2 L8 8 L15 2 M1 12 L6 7 M15 12 L10 7" fill="none" stroke="var(--ink)" stroke-width="1.4"/></svg>
        info@harborlinerelo.com
      </li>
    </ul>
    <p class="licensed">Licensed and Insured</p>
    <div class="services">
      <h2>Services</h2>
      <ul>
        <li>Local Moving</li>
        <li>Long Distance Moving</li>
        <li>Loading/Unloading your truck/container</li>
        <li>On-site Moving, Packing Service</li>
      </ul>
    </div>
  </section>

  <section class="card card-brand" aria-label="Card front with company name">
    <svg class="card-art" viewBox="0 0 700 400" aria-hidden="true">
      <defs>
        <linearGradient id="blueWedge" x1="0" y1="1" x2="1" y2="0">
          <stop offset="0" stop-color="var(--navy)"/>
          <stop offset="1" stop-color="var(--blue)"/>
        </linearGradient>
        <radialGradient id="redField" cx="0.8" cy="0.45" r="0.8">
          <stop offset="0" stop-color="var(--red)"/>
          <stop offset="1" stop-color="var(--red-deep)"/>
        </radialGradient>
      </defs>
      <path d="M0 396 C 300 330, 450 190, 520 0 L700 0 L700 400 L0 400 Z" fill="url(#blueWedge)"/>
      <path d="M10 400 C 320 340, 560 190, 700 8 L700 400 Z" fill="url(#redField)" stroke="var(--white)" stroke-width="3"/>
    </svg>
    <p class="brand-name">Harborline Relocation Group</p>
    <p class="brand-contact">www.HarborlineRelo.com<br>1-855-314-7068</p>
  </section>

</main>
</body>
</html>
```